Major Chiropractic Campaign Shown to 7 million people in print and online

Please design a SIMPLE and CLEAR advert in various sizes that will be used for print and media.

1/ Newspaper Print size: 381 x 272 with border and MUST be able to stand out in a newspaper

2/ Media: 5 sizes - rotating .gif 2 frames
- 160x600
- 728x90
- 300x250
- 300x600
- 320x50

3/ Facebook (must pass: http://tenthgridcheck.info)
- 300x315

Target Market(s)

females
35 - 54 yo
educated

Industry/Entity Type

Media

Font styles to use
Sans Serif

Colors
3176b5
33a6d7
ffffff
ec1f27
1b1b1b
919191
9bcb3c

Requirements
Must have
• clean
• easy to read
• strong CALL TO ACTION
• professional
• well designed book cover with the title " The Quiet Thread Linking Your Mind and Frame Revealed"
• The book MUST look like it's a professional report
• the winning design WILL show all design on a single page

```html
<!DOCTYPE html>
<html lang="en">
<head>
<meta charset="utf-8">
<title>Free Report – Skyscraper Banner</title>
<link rel="stylesheet" href="https://fonts.googleapis.com/css2?family=Archivo+Black&family=Roboto+Condensed:wght@700&family=Arimo:wght@400;700&display=swap">
<style>
  :root {
    --band-purple: #3a2a80;
    --band-blue: #1f8fd6;
    --bg-light: #f4f4f4;
    --bg-mid: #d9d9d9;
    --ink: #1b1b1b;
    --white: #ffffff;
    --cover-hot: #ec4a1f;
    --cover-deep: #a8231a;
    --spine: #c9c9c9;
  }
  * { margin: 0; padding: 0; box-sizing: border-box; }
  html, body { width: 1200px; height: 4520px; overflow: hidden; }
  body { font-family: "Arimo", Arial, sans-serif; }

  .banner {
    position: relative;
    width: 1200px;
    height: 4520px;
    overflow: hidden;
    background: linear-gradient(180deg, var(--bg-light) 0%, var(--bg-mid) 50%, var(--bg-light) 100%);
  }
  .bands { position: absolute; inset: 0; }

  .band-label {
    position: absolute;
    color: var(--white);
    font-family: "Archivo Black", "Arial Black", sans-serif;
    text-transform: uppercase;
    text-align: center;
    line-height: 0.95;
    letter-spacing: 4px;
  }
  .band-label--top {
    left: 515px; top: 250px;
    font-size: 150px;
    transform: translate(-50%, -50%) rotate(-34deg);
  }
  .band-label--bottom {
    left: 560px; top: 4080px;
    font-size: 165px;
    transform: translate(-50%, -50%) rotate(38deg);
  }

  /* Report cover */
  .report {
    position: absolute;
    left: 110px; top: 560px;
    width: 960px; height: 1330px;
  }
  .report__spine {
    position: absolute;
    left: 0; top: 30px;
    width: 50px; height: 1300px;
    background: linear-gradient(90deg, #b8b8b8, var(--spine));
  }
  .report__cover {
    position: absolute;
    left: 50px; top: 0;
    width: 910px; height: 1330px;
    background: radial-gradient(ellipse at 45% 50%, var(--cover-hot) 0%, #d43a1c 45%, var(--cover-deep) 100%);
    box-shadow: 0 30px 60px rgba(0,0,0,0.25);
    padding: 90px 60px 0 60px;
    color: var(--white);
  }
  .report__title {
    font-family: "Roboto Condensed", "Arial Narrow", sans-serif;
    font-weight: 700;
    font-size: 72px;
    line-height: 1.05;
  }
  .report__subtitle {
    font-family: "Arimo", Arial, sans-serif;
    font-weight: 400;
    font-size: 58px;
    line-height: 1.2;
    margin-top: 10px;
  }
  .report__art {
    position: absolute;
    left: 120px; top: 420px;
    width: 680px; height: 660px;
    border-radius: 46% 52% 40% 48%;
    background: radial-gradient(ellipse at 50% 50%, rgba(255,255,255,0.45) 0%, rgba(255,220,200,0.22) 45%, rgba(255,255,255,0) 72%);
  }
  .report__reflection {
    position: absolute;
    left: 110px; top: 1890px;
    width: 960px; height: 150px;
    background: linear-gradient(180deg, rgba(200,60,30,0.18), rgba(200,60,30,0));
  }

  /* Headline */
  .headline {
    position: absolute;
    left: 0; top: 2040px;
    width: 1200px;
    text-align: center;
    color: var(--ink);
    font-family: "Archivo Black", "Arial Black", sans-serif;
  }
  .headline__lead { font-size: 215px; line-height: 1; display: block; }
  .headline__body { font-size: 96px; line-height: 1.02; display: block; letter-spacing: 3px; margin-top: 10px; }
  .headline__close { font-size: 220px; line-height: 1.05; display: block; letter-spacing: 6px; }
</style>
</head>
<body>
  <main class="banner">
    <svg class="bands" width="1200" height="4520" viewBox="0 0 1200 4520" aria-hidden="true">
      <defs>
        <linearGradient id="bandGradient" x1="0" y1="0" x2="1" y2="0">
          <stop offset="0" stop-color="var(--band-purple)"/>
          <stop offset="1" stop-color="var(--band-blue)"/>
        </linearGradient>
      </defs>
      <polygon class="band-top-highlight" points="0,1000 1200,200 1200,300 0,1100" fill="#ffffff" opacity="0.8"/>
      <polygon class="band-top" points="0,0 1200,0 1200,200 0,1000" fill="url(#bandGradient)"/>
      <polygon class="band-bottom-highlight" points="0,2880 1200,3800 1200,3880 0,2960" fill="#ffffff" opacity="0.8"/>
      <polygon class="band-bottom" points="0,2960 1200,3880 1200,4520 0,4520" fill="url(#bandGradient)"/>
    </svg>

    <div class="band-label band-label--top">Free<br>Report</div>

    <div class="report">
      <div class="report__spine"></div>
      <div class="report__cover">
        <h2 class="report__title">The Quiet Thread</h2>
        <p class="report__subtitle">Linking Your Mind and Frame Revealed</p>
        <div class="report__art" role="img" aria-label="Glowing white line illustration of a brain on the red cover"></div>
      </div>
    </div>
    <div class="report__reflection"></div>

    <h1 class="headline">
      <span class="headline__lead">Doctors</span>
      <span class="headline__body">Explains Hidden<br>Connection that<br>Controls&nbsp;&nbsp;Your</span>
      <span class="headline__close">Health</span>
    </h1>

    <div class="band-label band-label--bottom">Get Free<br>Report</div>
  </main>
</body>
</html>
```